Project Sign for Construction Company

Site contractor needs a 4'x8' sign to place on construction sites for advertising. Our company builds the infrastructure for new housing developments. These sign will be posted on the road side to be viewed by passing cars. I want a clean and bold look and feel that resembles my company logo.

Font styles to use
Other font styles liked:
• Hypatia Sans Pro

Colors

Designer to choose colors to be used in the design.

Requirements
Must have
• 555-382-9146 | Info@MarlowPaving.example
• CUC 8047319
• www.MarlowPaving.example
• Services
• Road Construction
• Site Preparation & Excavation
• Underground Utilities
• Shoreline Restoration
Nice to have
• Now Hiring
• Pipe Layers
• Foremen
• Equipment Operators
Should not have
• Should not have stock picture images used in the design, focus on logo and geometric shapes

```html
<!DOCTYPE html>
<html lang="en">
<head>
<meta charset="utf-8">
<title>Marlow Paving – Site Sign</title>
<link rel="stylesheet" href="https://fonts.googleapis.com/css2?family=Arimo:wght@400;700&display=swap">
<style>
  :root {
    --brand-blue: #1a4a92;
    --band-grey: #6b6b6b;
    --text-dark: #1d1d1d;
    --tagline-grey: #666a70;
    --panel-white: #ffffff;
    --page-bg: #e6e6e6;
    --ghost-blue: #d7e1ee;
  }
  * { box-sizing: border-box; margin: 0; padding: 0; }
  html, body {
    width: 1200px; height: 1200px; overflow: hidden;
    background: var(--page-bg);
    font-family: "Arimo", Arial, sans-serif;
  }
  .canvas { position: relative; width: 1200px; height: 1200px; }
  .sign {
    position: absolute; left: 40px; top: 320px;
    width: 1044px; height: 522px;
    transform: scale(1.0728); transform-origin: 0 0;
    background: var(--panel-white);
    border: 1px solid #c9c9c9;
    overflow: hidden;
  }
  .sign-shapes { position: absolute; inset: 0; }
  .ghost-decoration {
    position: absolute; right: 0; top: 36px; width: 330px; height: 400px;
    background: radial-gradient(ellipse at 60% 45%, var(--ghost-blue) 0%, rgba(215,225,238,0.35) 55%, rgba(255,255,255,0) 80%);
  }
  .license {
    position: absolute; right: 42px; top: 7px;
    color: #fff; font-weight: 700; font-size: 22px; letter-spacing: 0.5px;
  }
  .brand { position: absolute; left: 92px; top: 78px; display: flex; align-items: center; gap: 26px; }
  .brand-mark { width: 96px; height: 96px; background: var(--brand-blue); flex: none; }
  .brand-text { display: flex; flex-direction: column; }
  .brand-name {
    color: var(--brand-blue); font-weight: 700; font-size: 62px; line-height: 1; letter-spacing: 2px;
    white-space: nowrap;
  }
  .brand-tagline {
    color: var(--tagline-grey); font-size: 30px; letter-spacing: 4px; margin-top: 10px;
    white-space: nowrap;
  }
  .column { position: absolute; top: 252px; }
  .column h2 {
    color: var(--brand-blue); font-weight: 700; font-size: 38px; line-height: 1.1; margin-left: 16px;
  }
  .column ul { list-style: none; margin-top: 2px; }
  .column li {
    color: var(--text-dark); font-size: 23px; line-height: 27px; position: relative; padding-left: 16px;
    white-space: nowrap;
  }
  .column li::before {
    content: ""; position: absolute; left: 2px; top: 11px;
    width: 7px; height: 7px; border-radius: 50%; background: var(--brand-blue);
  }
  .services { left: 62px; }
  .hiring { left: 455px; top: 251px; }
  .divider { position: absolute; left: 422px; top: 260px; width: 3px; height: 137px; background: var(--brand-blue); }
  .email { position: absolute; left: 498px; top: 418px; font-size: 21px; color: var(--text-dark); white-space: nowrap; }
  .phone {
    position: absolute; left: 34px; top: 442px;
    color: #fff; font-weight: 700; font-size: 58px; letter-spacing: 0.5px; white-space: nowrap;
  }
  .website {
    position: absolute; left: 522px; top: 461px;
    color: #fff; font-size: 38px; white-space: nowrap;
  }
</style>
</head>
<body>
<div class="canvas">
  <div class="sign">
    <div class="ghost-decoration" role="img" aria-label="Faint oversized brand decoration area"></div>
    <svg class="sign-shapes" width="1044" height="522" viewBox="0 0 1044 522" aria-hidden="true">
      <polygon points="0,0 70,0 88,36 0,36" fill="var(--band-grey)"/>
      <polygon points="240,0 1044,0 1044,36 258,36" fill="var(--brand-blue)"/>
      <polygon points="0,435 455,435 500,512 0,512" fill="var(--brand-blue)"/>
      <polygon points="472,452 1044,452 1044,512 510,512" fill="var(--band-grey)"/>
    </svg>
    <div class="license">CUC 8047319</div>
    <div class="brand">
      <div class="brand-mark"></div>
      <div class="brand-text">
        <div class="brand-name">MARLOW PAVING</div>
        <div class="brand-tagline">CIVIL CONSTRUCTION</div>
      </div>
    </div>
    <div class="column services">
      <h2>Services</h2>
      <ul>
        <li>Road Construction</li>
        <li>Site Preparation &amp; Excavation</li>
        <li>Underground Utilities</li>
        <li>Shoreline Restoration</li>
      </ul>
    </div>
    <div class="divider"></div>
    <div class="column hiring">
      <h2>Now Hiring</h2>
      <ul>
        <li>Pipe Layers</li>
        <li>Foremen</li>
        <li>Equipment Operators</li>
      </ul>
    </div>
    <div class="email">Info@MarlowPaving.example</div>
    <div class="phone">555-382-9146</div>
    <div class="website">www.MarlowPaving.example</div>
  </div>
</div>
</body>
</html>
```